Consultant Firm Marketing Flyer

I want to use this flyer to market health care consultant services. I would like a front and back glossy, professional, yet bold and eye catching design. I would like it to convey knowledge, expertise, partnership and strength. The colors should blue and white but I am very open to the designer being creative. You can visit my website to see colors and images I want to use at brightwaveadvisory.net
I would like the home page image on my website to be incorporated into the flyer but I am also open to other images that work with the design. The designer can be creative.

I want to highlight 4 service area’s of focus to my clients:
1. Revenue Cycle Optimization (making my clients money)
2. Practice Management Optimization (improving clinical operations)
3. Health Compliance (following the law)
4. Health Care Technology: (Telemedicine and AI)
Please be creative. Go where ever your creativity leads.

```html
<!DOCTYPE html>
<html lang="en">
<head>
<meta charset="utf-8">
<title>Brightwave Advisory Flyer</title>
<link href="https://fonts.googleapis.com/css2?family=Poppins:wght@500;600;700&family=Open+Sans:ital,wght@0,400;0,600;0,700;1,700&display=swap" rel="stylesheet">
<style>
:root{
  --stage:#9b9b9b;
  --blue:#0a4f9f;
  --blue-deep:#06428a;
  --blue-bright:#1f6fc4;
  --sky:#2a9be0;
  --white:#ffffff;
  --ink:#1c1c1c;
  --muted:#3a3a3a;
  --rule:#c9ced6;
}
*{margin:0;padding:0;box-sizing:border-box}
html,body{width:1200px;height:1000px;overflow:hidden;background:var(--stage)}
body{position:relative;font-family:"Open Sans",Arial,sans-serif;color:var(--ink)}
.page{position:absolute;top:143px;width:553px;height:715px;background:var(--white);overflow:hidden}
.page--front{left:38px}
.page--back{left:609px}

.brand{position:absolute;display:flex;flex-direction:column;align-items:center;gap:6px;white-space:nowrap}
.brand__mark{width:12px;height:12px;border-radius:50%;background:var(--blue)}
.brand__name{font-family:"Poppins",Arial,sans-serif;font-weight:600;font-size:13px;color:var(--blue);letter-spacing:.3px}
.page--front .brand{left:0;right:0;top:34px}
.page--back .brand{left:252px;top:34px;width:180px}

/* front */
.hero{position:absolute;left:0;top:100px;width:553px;height:335px;
  background:linear-gradient(180deg,#5d6670 0%,#3e464f 55%,#2e353d 100%)}
.hero__shade{position:absolute;inset:0;background:linear-gradient(180deg,rgba(10,20,35,.15),rgba(10,20,35,.45))}
.hero__url{position:absolute;left:0;right:0;text-align:center;font-family:"Poppins",Arial,sans-serif;font-weight:600;font-size:11px;letter-spacing:3px;color:var(--white)}
.hero__title{position:absolute;left:0;right:0;text-align:center;font-family:"Poppins",Arial,sans-serif;font-weight:600;font-size:34px;line-height:43px;color:var(--white)}
.hero__bar{position:absolute;left:258px;width:38px;height:4px;background:var(--blue-bright)}
.hero__lede{position:absolute;left:85px;width:383px;text-align:center;font-size:11px;line-height:13px;color:var(--white)}
.banner{position:absolute;left:0;top:435px;width:553px;height:42px;background:var(--blue);
  font-family:"Poppins",Arial,sans-serif;font-weight:600;font-size:19px;color:var(--white);text-align:center;line-height:42px}
.banner__notch{position:absolute;left:268px;top:477px;width:0;height:0;border-left:9px solid transparent;border-right:9px solid transparent;border-top:9px solid var(--blue)}
.services{position:absolute;left:35px;top:507px;display:flex;gap:7px}
.service{width:115px;height:113px;background:var(--white);box-shadow:0 2px 8px rgba(0,0,0,.14);border-bottom:4px solid var(--sky);
  display:flex;flex-direction:column;align-items:center;padding-top:16px;color:var(--blue-bright)}
.service svg{width:38px;height:38px}
.service__name{margin-top:12px;font-family:"Poppins",Arial,sans-serif;font-weight:500;font-size:12.5px;line-height:14px;color:var(--blue);text-align:center}
.footer{position:absolute;left:0;top:650px;width:553px;height:65px;background:var(--blue);border-top:3px solid var(--sky);color:var(--white)}
.footer__call{position:absolute;left:34px;top:14px;display:flex;gap:10px}
.footer__label{font-family:"Poppins",Arial,sans-serif;font-size:12px;font-weight:500}
.footer__phone{position:absolute;left:58px;top:28px;font-family:"Poppins",Arial,sans-serif;font-weight:600;font-size:17px;white-space:nowrap}
.footer__divider{position:absolute;left:233px;top:12px;height:40px;border-left:1px dashed rgba(255,255,255,.5)}
.footer__info{position:absolute;left:278px;top:12px;font-size:9px;line-height:12px}
.footer__web{font-family:"Poppins",Arial,sans-serif;font-weight:600;font-size:11px;line-height:14px}
.footer__social{position:absolute;left:472px;top:34px;display:flex;gap:5px}
.footer__social span{width:11px;height:11px;border-radius:50%;background:var(--white)}

/* back */
.side-photo{position:absolute;left:0;top:0;width:236px;height:715px;
  background:linear-gradient(180deg,#c7d3de 0%,#9fb0c1 35%,#53657a 65%,#cfd6dd 100%)}
.side-photo__shade{position:absolute;inset:0;background:linear-gradient(180deg,rgba(20,40,70,.25),rgba(20,40,70,.05) 50%,rgba(255,255,255,.1))}
.side-title{position:absolute;right:342px;top:76px;width:200px;text-align:right;font-family:"Poppins",Arial,sans-serif;font-weight:600;font-size:19px;line-height:24px;color:var(--white)}
.side-title__bar{position:absolute;left:230px;top:80px;width:6px;height:62px;background:var(--blue)}
.side-contact{position:absolute;left:0;top:642px;width:236px;height:38px;background:rgba(255,255,255,.18);
  font-family:"Poppins",Arial,sans-serif;font-weight:600;font-size:13px;line-height:38px;text-align:right;padding-right:24px;color:var(--white)}
.side-contact span{color:var(--blue-bright)}
.solutions{position:absolute;left:272px;top:94px;width:250px}
.solutions__title{font-family:"Poppins",Arial,sans-serif;font-weight:600;font-size:24px;color:var(--blue)}
.solutions__intro{margin-top:6px;font-size:8.5px;line-height:11px;font-weight:700;font-style:italic;color:var(--ink)}
.item{position:absolute;left:294px;width:225px}
.item__title{font-family:"Poppins",Arial,sans-serif;font-weight:600;font-size:13px;color:var(--blue)}
.item__text{margin-top:3px;font-size:8.5px;line-height:10.6px;color:var(--muted)}
.item__rule{position:absolute;left:294px;width:196px;border-top:1px dashed var(--rule)}
.badge{position:absolute;left:188px;width:92px;height:92px;border-radius:50%;background:var(--white);
  display:flex;align-items:center;justify-content:center}
.badge__disc{width:76px;height:76px;border-radius:50%;background:var(--blue);display:flex;align-items:center;justify-content:center;color:var(--white)}
.badge svg{width:38px;height:38px}
.address{position:absolute;left:272px;top:630px;font-size:8.8px;line-height:10.8px;color:var(--ink)}
.address__name{font-weight:600;font-size:11px;line-height:14px}
.address b{font-weight:600}
.address .accent{color:var(--blue);font-weight:600}
</style>
</head>
<body>

<svg width="0" height="0" style="position:absolute">
  <defs>
    <symbol id="icon-cycle" viewBox="0 0 40 40">
      <g fill="none" stroke="currentColor" stroke-width="1.6" stroke-linecap="round" stroke-linejoin="round">
        <path d="M9 16a12 12 0 0 1 18-7"/><path d="M27 5v4h-4"/>
        <path d="M31 24a12 12 0 0 1-18 7"/><path d="M13 35v-4h4"/>
        <path d="M8 22a12 12 0 0 0 3 7"/><path d="M32 18a12 12 0 0 0-3-7"/>
      </g>
    </symbol>
    <symbol id="icon-doc" viewBox="0 0 40 40">
      <g fill="none" stroke="currentColor" stroke-width="1.6" stroke-linecap="round" stroke-linejoin="round">
        <rect x="10" y="6" width="20" height="28" rx="1"/>
        <path d="M14 12h12M14 17h12M14 22h8M14 27h6"/>
        <path d="M24 28l2 2 5-5"/>
      </g>
    </symbol>
    <symbol id="icon-tech" viewBox="0 0 40 40">
      <g fill="none" stroke="currentColor" stroke-width="1.6" stroke-linecap="round" stroke-linejoin="round">
        <rect x="5" y="7" width="30" height="20" rx="1.5"/>
        <path d="M15 33h10M20 27v6"/>
        <path d="M11 17h5l2-4 3 8 2-4h6"/>
      </g>
    </symbol>
    <symbol id="icon-team" viewBox="0 0 40 40">
      <g fill="none" stroke="currentColor" stroke-width="1.6" stroke-linecap="round" stroke-linejoin="round">
        <path d="M20 4v10M16 8l4-4 4 4"/>
        <path d="M10 8v8M7 11l3-3 3 3"/>
        <path d="M30 8v8M27 11l3-3 3 3"/>
        <circle cx="20" cy="21" r="3"/><path d="M14 34v-3a6 6 0 0 1 12 0v3"/>
        <circle cx="9" cy="24" r="2.5"/><path d="M4 34v-2a5 5 0 0 1 8-4"/>
        <circle cx="31" cy="24" r="2.5"/><path d="M36 34v-2a5 5 0 0 0-8-4"/>
      </g>
    </symbol>
  </defs>
</svg>

<section class="page page--front">
  <div class="brand"><span class="brand__mark"></span><span class="brand__name">Brightwave Advisory LLC</span></div>

  <div class="hero" role="img" aria-label="Photo of a diverse team of healthcare professionals meeting around a table in a bright office">
    <div class="hero__shade"></div>
  </div>
  <div class="hero__url" style="top:180px">www.brightwaveadvisory.net</div>
  <h1 class="hero__title" style="top:204px">Advancing Healthcare<br>Operations</h1>
  <div class="hero__bar" style="top:298px"></div>
  <p class="hero__lede" style="top:316px">Brightwave Advisory (BWA) is a healthcare consulting firm skilled at helping physician practices advance their strategic vision in an ever-evolving healthcare system.</p>

  <div class="banner">Expertise your medical practice deserves</div>
  <div class="banner__notch"></div>

  <div class="services">
    <div class="service"><svg><use href="#icon-cycle"/></svg><div class="service__name">Revenue Cycle<br>Management</div></div>
    <div class="service"><svg><use href="#icon-doc"/></svg><div class="service__name">Regulatory<br>Compliance</div></div>
    <div class="service"><svg><use href="#icon-tech"/></svg><div class="service__name">Health Care<br>Technology</div></div>
    <div class="service"><svg><use href="#icon-team"/></svg><div class="service__name">Practice<br>Management</div></div>
  </div>

  <footer class="footer">
    <div class="footer__call">
      <svg width="14" height="14" viewBox="0 0 24 24" fill="none" stroke="#fff" stroke-width="1.8" stroke-linejoin="round"><path d="M5 3h4l2 5-3 2a12 12 0 0 0 6 6l2-3 5 2v4a2 2 0 0 1-2 2A17 17 0 0 1 3 5a2 2 0 0 1 2-2z"/></svg>
      <span class="footer__label">CALL US:</span>
    </div>
    <div class="footer__phone">(555) 214-0736</div>
    <div class="footer__divider"></div>
    <div class="footer__info">
      <div class="footer__web">www.brightwaveadvisory.net</div>
      <div>118 Harbor Lane, Easton, ST 20451, USA</div>
      <div>Mail: <b>info@brightwaveadvisory.net</b></div>
    </div>
    <div class="footer__social"><span></span><span></span><span></span></div>
  </footer>
</section>

<section class="page page--back">
  <div class="side-photo" role="img" aria-label="Photo of two colleagues reviewing work together at a laptop in a bright office">
    <div class="side-photo__shade"></div>
  </div>
  <div class="side-title">Expertise Your<br>Medical Practice<br>Deserves</div>
  <div class="side-title__bar"></div>
  <div class="side-contact">Contact <span>Us</span></div>

  <div class="brand"><span class="brand__mark"></span><span class="brand__name">Brightwave Advisory LLC</span></div>

  <div class="solutions">
    <h2 class="solutions__title">Solutions</h2>
    <p class="solutions__intro">The varied expertise of our team encompass full service revenue cycle management, practice management, regulatory compliance, health care technology, and full spectrum health care consulting services.</p>
  </div>

  <div class="badge" style="top:192px"><div class="badge__disc"><svg><use href="#icon-cycle"/></svg></div></div>
  <div class="item" style="top:198px">
    <h3 class="item__title">Revenue Cycle Management</h3>
    <p class="item__text">In today's increasingly complex health care environment it's important now more than ever that medical practices closely manage their revenue cycle. Brightwave Advisory (BWA) understands the reimbursement landscape</p>
  </div>
  <div class="item__rule" style="top:290px"></div>

  <div class="badge" style="top:301px"><div class="badge__disc"><svg><use href="#icon-doc"/></svg></div></div>
  <div class="item" style="top:306px">
    <h3 class="item__title">Regulatory Compliance</h3>
    <p class="item__text">In a heavily regulated healthcare environment medical practices need to be acutely aware of regulations as they present huge liabilities. It is extremely important to ensure compliance with regulations. BWA offers a host of comprehensive compliance services.</p>
  </div>
  <div class="item__rule" style="top:399px"></div>

  <div class="badge" style="top:409px"><div class="badge__disc"><svg><use href="#icon-tech"/></svg></div></div>
  <div class="item" style="top:414px">
    <h3 class="item__title">Health Care Technology</h3>
    <p class="item__text">Telemedicine and AI are changing how care is delivered. BWA helps your practice choose, implement and optimize virtual visit platforms and AI tools that improve access, streamline workflows and support better outcomes for your medical practice.</p>
  </div>
  <div class="item__rule" style="top:507px"></div>

  <div class="badge" style="top:517px"><div class="badge__disc"><svg><use href="#icon-team"/></svg></div></div>
  <div class="item" style="top:522px">
    <h3 class="item__title">Practice Management</h3>
    <p class="item__text">Practice Management is challenging and it requires the right balance of skill, knowledge, experience and management expertise. BWA Offers assessment and optimization in Patient Access &amp; Scheduling, Patient Experience, Staff Experience.</p>
  </div>

  <div class="address">
    <div class="address__name">Brightwave Advisory</div>
    <div>118 Harbor Lane, Easton, ST 20451, USA</div>
    <div><b>Phone:</b> <span class="accent">(555) 214-0736</span></div>
    <div><b>Website:</b> www.brightwaveadvisory.net</div>
    <div><b>Mail:</b> info@brightwaveadvisory.net</div>
  </div>
</section>

</body>
</html>
```